Catalogue des écoles de langues partenaires de Morvaleck

Who are we ?
The group has 3 Morvaleck training facilities that could be established in Tunisia in recent years: Morvaleck, Bristane and Pluvemor.
What do we offer?
A wide range of services for all those interested in the German language training, career counseling, translation, assitance start ... The Morvaleck group offers help at every stage.
We need a new 2016 catalog of language schools Morvaleck partners in our business.
This is based on the old catalog 2015, but with some modifications, including the Design level, catalog text and the list of partner schools that will be updated.
The idea is to make this catalog a guide that comes in direct contact with the customer that will read the catalog.
The purpose of this catalog is to create a direct relationship with the customer who will read to choose later the city and school that suit him.
The catalog contains roughly 3/4 sections:
* 1st section: the first pages "standards" of our brochure, here we leave the old model to add a few details and change the design and organization;
the logo, the German flag, catalog name, address for making contact with Morvaleck,
the summary, the map of Germany with cities on the departments where Morvaleck has partner schools
All this will not fail in our catalog
*2nd section:
Presentation cities where Morvaleck partner language schools are located
Here is a description of the city, pictures of the city and language schools list without going into details of each school
3rd section:
Part 1: Overview of language schools partner Morvaleck by our "guide" team that will accompany us in this section, there will be a representative from each school that is located in several cities
An overview of the school, the services (we leave the old model), the location of the school in every German city (google map photo), housing highlighted !!!!
The cultural prog perhaps?
Part 2: everything about the course:
max number of people in each class levels (page 3 of the old model), review KLO Centre or not, units per week, intensive courses, super intensive courses, prices ???course dates,
dsh - daf difference? Registration tips, links, ... a few tips
Quote " Ubung macht den Meister " for example
* 4th section and last section:
under the title of "1st Steps in Germany"
* What to do upon arrival
* Basic vocabulary (discussion circle, representatives from each school)
* Say goodbye, good luck .. Germany, photo, dream, travel ..
> Sayings of the whole team and bubbles!!!!
> We would like a design in shades of green of our logo !! (really important)
We take the example of a page of this catalog in this section.
The page consists of several parts:
School description, super intensive and intensive courses
Date of the beginning and the end of each session in this school
School Location (pictured google map)
A table that includes:
Room, kitchen, linen and towels, common area, distance to campus , the prices ,units per week
(See attached file )

```html
<!DOCTYPE html>
<html lang="fr">
<head>
<meta charset="utf-8">
<title>Morvaleck — Catalogue 2016, quatrième de couverture</title>
<link href="https://fonts.googleapis.com/css2?family=Arimo:wght@400;700&display=swap" rel="stylesheet">
<style>
  :root{
    --backdrop:#ebe8e3;
    --paper:#ffffff;
    --ink:#2b2b2b;
    --accent-lime:#d6d618;
    --photo-dark:#4a3c34;
    --photo-mid:#7c6a5e;
    --photo-light:#a9a7a8;
    --partner-green:#9cc21c;
    --partner-navy:#1a4a8c;
    --partner-blue:#1f5fae;
    --partner-teal:#5f8f8c;
    --partner-royal:#1e3fa0;
  }
  *{margin:0;padding:0;box-sizing:border-box}
  html,body{width:1200px;height:1200px;overflow:hidden}
  body{background:var(--backdrop);font-family:"Arimo",Arial,sans-serif;color:var(--ink)}
  .back-cover{position:absolute;left:197px;top:30px;width:806px;height:1140px;background:var(--paper);box-shadow:0 2px 10px rgba(0,0,0,.15)}
  .offices{position:absolute;right:46px;top:252px;text-align:right;font-size:15.7px;line-height:18.3px}
  .office + .office{margin-top:18px}
  .office-name{font-weight:700}
  .photo-band{position:absolute;left:0;top:570px;width:806px;height:285px;display:flex}
  .photo-band .accent-strip{width:46px;background:var(--accent-lime)}
  .photo-band .photo{flex:1;background:linear-gradient(180deg,var(--photo-light) 0%,var(--photo-mid) 45%,var(--photo-dark) 100%)}
  .partners-title{position:absolute;right:46px;top:897px;font-weight:700;font-size:16.5px}
  .partner{position:absolute;display:flex;align-items:center;gap:6px;font-weight:700;font-size:12px;line-height:1.05}
  .partner .mark{width:14px;height:14px;border-radius:50%;flex:none}
  .partner .mark.square{border-radius:0}
  .p-veltrana{left:433px;top:934px;color:var(--partner-green)}
  .p-veltrana .mark{background:var(--partner-green)}
  .p-lindqvar{left:549px;top:926px;color:var(--partner-navy)}
  .p-lindqvar .mark{width:44px;height:44px;background:var(--partner-navy)}
  .p-pluvemor{left:686px;top:940px;color:var(--partner-teal)}
  .p-pluvemor .mark{background:var(--partner-teal)}
  .p-halvern{left:359px;top:1000px;color:var(--partner-blue);font-size:13px}
  .p-quorell{left:485px;top:998px;color:var(--partner-blue);font-size:13px}
  .p-quorell .mark{width:20px;height:20px;background:var(--partner-blue)}
  .p-astrevo{left:618px;top:993px;width:140px;height:16px;justify-content:center;background:var(--partner-royal);color:#fff;font-size:13px}
</style>
</head>
<body>
  <main class="back-cover">
    <section class="offices">
      <address class="office" style="font-style:normal">
        <div class="office-name">Morvaleck à Tunis</div>
        <div>Imm. les Cèdres, 3ème étage</div>
        <div>27 Rue du Lac Vendrel</div>
        <div>1053, Les Rives du Lac 1</div>
        <div>(En face de l’Hotel Solvane)</div>
        <div>Tél.: 71 000 482</div>
        <div>E-mail: tunis [@] morvaleck.org</div>
      </address>
      <address class="office" style="font-style:normal">
        <div class="office-name">Morvaleck à Sfax</div>
        <div>Imm. Yasmine, 5ème étage Av. de l’Aurore</div>
        <div>Rue Habib Marzouk</div>
        <div>(derrière la faculté des sciences)</div>
        <div>3000, Sfax</div>
        <div>Tél.: 74 000 716</div>
        <div>E-mail: sfax [@] morvaleck.org</div>
      </address>
    </section>

    <div class="photo-band">
      <div class="accent-strip"></div>
      <div class="photo" role="img" aria-label="Photo de jeunes étudiants assis côte à côte sur un banc avec tablettes et ordinateur portable"></div>
    </div>

    <h2 class="partners-title">Partenaires officiels</h2>
    <div class="partner p-veltrana"><span class="mark"></span><span>VELTRANA<br>INSTITUT</span></div>
    <div class="partner p-lindqvar"><span class="mark square"></span><span>LINDQVAR<br>SPRACH<br>SCHULE</span></div>
    <div class="partner p-pluvemor"><span class="mark square"></span><span>PLUVEMOR</span></div>
    <div class="partner p-halvern"><span>Halvern Akademie</span></div>
    <div class="partner p-quorell"><span class="mark square"></span><span>QUORELL</span></div>
    <div class="partner p-astrevo"><span>ASTREVO</span></div>
  </main>
</body>
</html>
```